R & T Summit Construction Business Card ideas

We want a business card to represents our company in a way that looks professional but is also a business card that is unique!

Industry/Entity Type

Construction Company

Contact Information for Business Card

open to all design ideas, just want to be able to see different options to choose from in either color or grayscale.

Requirements
Must have
• Our names and phone numbers
• Mark Hollis 386-555-0142
• Derek Walsh 386-555-0187
• Business logo

```html
<!DOCTYPE html>
<html lang="en">
<head>
<meta charset="utf-8">
<title>R &amp; T Summit Construction – Business Card</title>
<link href="https://fonts.googleapis.com/css2?family=Mulish:wght@600;700;800&display=swap" rel="stylesheet">
<style>
  :root {
    --paper: #ffffff;
    --blue-bright: #0a3dfb;
    --blue-mid: #0d2a9e;
    --navy: #04325f;
    --ink: #0b0b0d;
    --title-grey: #8e989e;
    --detail-grey: #b3bbc1;
    --brand: #0d2a9e;
  }
  html, body {
    margin: 0;
    padding: 0;
    overflow: hidden;
    background: var(--paper);
  }
  .card {
    position: relative;
    width: 1200px;
    height: 686px;
    overflow: hidden;
    background: var(--paper);
    font-family: "Mulish", "Century Gothic", sans-serif;
  }
  .card__waves {
    position: absolute;
    inset: 0;
    width: 1200px;
    height: 686px;
  }
  .brand {
    position: absolute;
    left: 230px;
    top: 343px;
    transform: translate(-50%, -50%) rotate(-90deg);
    display: flex;
    align-items: center;
    gap: 18px;
    white-space: nowrap;
  }
  .brand__mark {
    width: 30px;
    height: 30px;
    background: var(--brand);
  }
  .brand__name {
    font-size: 38px;
    font-weight: 800;
    color: var(--brand);
    letter-spacing: 1px;
  }
  .contact {
    position: absolute;
  }
  .contact--derek { left: 781px; top: 44px; }
  .contact--mark  { left: 617px; top: 362px; }
  .contact__name {
    margin: 0;
    font-size: 33px;
    font-weight: 800;
    color: var(--ink);
    letter-spacing: 1.5px;
    text-transform: uppercase;
    line-height: 1.1;
  }
  .contact__role {
    margin: 2px 0 0;
    font-size: 25px;
    font-weight: 700;
    color: var(--title-grey);
    letter-spacing: 0.6px;
    text-transform: uppercase;
    line-height: 1.2;
  }
  .contact__list {
    list-style: none;
    margin: 24px 0 0;
    padding: 0;
  }
  .contact__item {
    display: flex;
    align-items: center;
    height: 34px;
    font-size: 25px;
    font-weight: 700;
    color: var(--detail-grey);
    letter-spacing: 0.3px;
  }
  .contact__icon {
    width: 22px;
    height: 22px;
    margin-right: 38px;
    flex: none;
  }
  .contact__item--address {
    padding-left: 60px;
    height: 34px;
    font-weight: 600;
    color: var(--detail-grey);
  }
  .contact--mark .contact__icon { margin-right: 21px; }
  .contact--mark .contact__item--address { padding-left: 43px; }
</style>
</head>
<body>
<div class="card">
  <svg class="card__waves" viewBox="0 0 1050 600" preserveAspectRatio="none" aria-hidden="true">
    <path d="M440 0 C382 150 368 420 445 600 L1050 600 L1050 0 Z" fill="var(--blue-bright)"/>
    <path d="M548 0 C445 140 422 420 478 600 L1050 600 L1050 0 Z" fill="var(--blue-mid)"/>
    <path d="M655 0 C510 110 455 380 502 600 L1050 600 L1050 0 Z" fill="var(--navy)"/>
  </svg>

  <div class="brand">
    <span class="brand__mark"></span>
    <span class="brand__name">R &amp; T Summit Construction</span>
  </div>

  <section class="contact contact--derek">
    <h2 class="contact__name">Derek Walsh</h2>
    <p class="contact__role">Managing Director</p>
    <ul class="contact__list">
      <li class="contact__item">
        <svg class="contact__icon" viewBox="0 0 24 24"><path d="M6.6 2.5 9.4 6.6 7.6 8.7c1.2 2.8 4.3 6 7.6 7.6l2-1.9 4.2 2.8-1.3 3.6C11.4 21.2 2.8 12.6 3 3.8Z" fill="var(--ink)"/></svg>
        386-555-0187
      </li>
      <li class="contact__item">
        <svg class="contact__icon" viewBox="0 0 24 24"><path d="M2 9 22 3 15 21 12 13Z" fill="var(--ink)"/></svg>
        hello@rtsummit.com
      </li>
      <li class="contact__item">
        <svg class="contact__icon" viewBox="0 0 24 24"><circle cx="12" cy="12" r="10" fill="var(--ink)"/><path d="M2 12h20M12 2v20M5 6.5h14M5 17.5h14" stroke="var(--navy)" stroke-width="1.3" fill="none"/><ellipse cx="12" cy="12" rx="4.5" ry="10" stroke="var(--navy)" stroke-width="1.3" fill="none"/></svg>
        www.rtsummit.com
      </li>
      <li class="contact__item contact__item--address">Here your company</li>
      <li class="contact__item contact__item--address">or home address</li>
    </ul>
  </section>

  <section class="contact contact--mark">
    <h2 class="contact__name">Mark Hollis</h2>
    <p class="contact__role">Managing Director</p>
    <ul class="contact__list">
      <li class="contact__item">
        <svg class="contact__icon" viewBox="0 0 24 24"><path d="M6.6 2.5 9.4 6.6 7.6 8.7c1.2 2.8 4.3 6 7.6 7.6l2-1.9 4.2 2.8-1.3 3.6C11.4 21.2 2.8 12.6 3 3.8Z" fill="var(--ink)"/></svg>
        386-555-0142
      </li>
      <li class="contact__item">
        <svg class="contact__icon" viewBox="0 0 24 24"><path d="M2 9 22 3 15 21 12 13Z" fill="var(--ink)"/></svg>
        hello@rtsummit.com
      </li>
      <li class="contact__item">
        <svg class="contact__icon" viewBox="0 0 24 24"><circle cx="12" cy="12" r="10" fill="var(--ink)"/><path d="M2 12h20M12 2v20M5 6.5h14M5 17.5h14" stroke="var(--navy)" stroke-width="1.3" fill="none"/><ellipse cx="12" cy="12" rx="4.5" ry="10" stroke="var(--navy)" stroke-width="1.3" fill="none"/></svg>
        www.rtsummit.com
      </li>
      <li class="contact__item contact__item--address">Here your company</li>
      <li class="contact__item contact__item--address">or home address</li>
    </ul>
  </section>
</div>
</body>
</html>
```